Maple Creek Food and Supply - Raw Dog Food Delivery Truck**

Design a small delivery truck wrap for Maple Creek Food and Supply.
We want the truck to be humorous or clever so that people around town/state will recognize it and talk about it like: “Hey did you see the Maple Creek truck in town? Isn’t it funny/cute/great?”
We are an e-commerce business that sells directly to consumers - dog owners. So our website url or QR Code is important.

Target Market(s)

Dog owners; dog owners who feed their dogs raw food; dog owners who are willing try raw dog food; owners who want to learn more about the benefits of raw feeding.

Requirements
Must have
• We think we want our website's QR Code and our website's url.
Nice to have
• We want it to be bright
We want to have a medium to large, cute dog that will attract people’s eyes to it.
We want to have a short catchy phrase. Something like:
- Just Chew it! (a shoe company takeoff)
- Get Real. Get Raw.
- Real Dogs Eat Raw
- Feed me raw. I’ll lick you later.
We may need to proceed any short phrase with a message for those who don’t know anything about raw feeding, such as:
For a Healthy & Happy Dog…

```html
<!DOCTYPE html>
<html lang="en">
<head>
<meta charset="utf-8">
<title>Maple Creek Food and Supply – Truck Wrap</title>
<link href="https://fonts.googleapis.com/css2?family=Baloo+2:wght@700;800&family=Arvo:wght@700&display=swap" rel="stylesheet">
<style>
  :root{
    --page:#6f6f6f;
    --white:#ffffff;
    --cyan:#6fc9df;
    --ink:#1c2226;
    --brown:#231916;
    --olive:#24251a;
    --lime:#b7d63a;
    --grass-dark:#1f3a1a;
    --grass-mid:#3f6a26;
    --grass-light:#8cc43b;
  }
  *{margin:0;padding:0;box-sizing:border-box}
  html,body{width:960px;height:1200px;overflow:hidden;background:var(--page)}
  .wrap{
    position:absolute;left:40px;top:450px;width:880px;height:300px;
    overflow:hidden;box-shadow:0 18px 22px -14px rgba(0,0,0,.45);
  }
  .wrap__photo{
    position:absolute;inset:0;
    background:
      radial-gradient(ellipse 120px 150px at 610px 130px,#e9e2d6 0%,#cfb596 45%,rgba(207,181,150,0) 75%),
      linear-gradient(180deg,rgba(0,0,0,0) 55%,var(--grass-light) 72%,#6fae2e 100%),
      linear-gradient(90deg,var(--grass-dark) 0%,var(--grass-mid) 45%,#50702e 75%,#7c9a3c 100%);
  }
  .headline{
    position:absolute;left:26px;top:18px;
    font-family:"Baloo 2",sans-serif;font-weight:700;
    font-size:35px;line-height:38px;color:var(--white);
  }
  .question{
    position:absolute;left:26px;top:108px;
    font-family:"Arvo",serif;font-weight:700;font-size:37px;color:var(--white);
  }
  .slogan-band{
    position:absolute;left:0;top:181px;width:346px;height:50px;
    background:var(--cyan);clip-path:polygon(0 0,100% 0,84% 100%,0 100%);
  }
  .slogan{
    position:absolute;left:26px;top:181px;height:50px;line-height:54px;
    font-family:"Baloo 2",sans-serif;font-weight:800;font-size:33px;color:var(--ink);
  }
  .url-band{
    position:absolute;left:0;top:232px;width:540px;height:68px;
    background:var(--brown);clip-path:polygon(0 0,95% 0,100% 100%,0 100%);
  }
  .url{
    position:absolute;left:24px;top:232px;height:54px;
    display:flex;align-items:center;gap:8px;
    font-family:"Arvo",serif;font-weight:700;font-size:22px;color:var(--white);
  }
  .url svg{width:28px;height:28px}
  .tagline-band{
    position:absolute;left:515px;top:250px;width:365px;height:50px;
    background:var(--olive);clip-path:polygon(0 0,100% 0,100% 100%,6% 100%);
  }
  .tagline-edge{
    position:absolute;left:515px;top:250px;width:40px;height:50px;
    background:var(--lime);clip-path:polygon(0 0,8% 0,22% 100%,14% 100%);
  }
  .tagline{
    position:absolute;right:20px;top:250px;height:50px;line-height:52px;
    font-family:"Arvo",serif;font-weight:700;font-size:20px;color:var(--white);
  }
  .brand{
    position:absolute;left:718px;top:30px;width:128px;text-align:center;
    font-family:"Arvo",serif;font-weight:700;font-size:26px;line-height:30px;color:var(--white);
  }
  .brand__box{
    width:14px;height:14px;border:2px solid var(--white);margin:8px auto 0;
  }
</style>
</head>
<body>
  <section class="wrap">
    <div class="wrap__photo" role="img" aria-label="Photo of a small white and tan terrier running across a sunny lawn with a spiky yellow ball in its mouth, blurred green trees behind"></div>

    <h1 class="headline">Hey did you see the<br>Maple Creek truck in town?</h1>
    <p class="question">Isn’t it Funny ?</p>

    <div class="slogan-band"></div>
    <p class="slogan">JUST CHEW IT!</p>

    <div class="url-band"></div>
    <p class="url">
      <svg viewBox="0 0 28 28" aria-hidden="true">
        <circle cx="14" cy="14" r="12.5" fill="none" stroke="#fff" stroke-width="2"/>
        <circle cx="14" cy="14" r="8.5" fill="none" stroke="#fff" stroke-width="1.4"/>
        <ellipse cx="14" cy="14" rx="3.8" ry="8.5" fill="none" stroke="#fff" stroke-width="1.2"/>
        <line x1="5.5" y1="14" x2="22.5" y2="14" stroke="#fff" stroke-width="1.2"/>
        <line x1="7" y1="10" x2="21" y2="10" stroke="#fff" stroke-width="1"/>
        <line x1="7" y1="18" x2="21" y2="18" stroke="#fff" stroke-width="1"/>
      </svg>
      www.maplecreekfoodandsupply.com
    </p>

    <div class="tagline-band"></div>
    <div class="tagline-edge"></div>
    <p class="tagline">For a Healthy &amp; Happy Dog</p>

    <div class="brand">
      MAPLE<br>CREEK
      <div class="brand__box"></div>
    </div>
  </section>
</body>
</html>
```